Cafe Business needs a business card design

I already have an ai logo I would like to use and color. I need someone to make a business card for me on adobe illustrator with it. Its for a cafe restaurant opening in Japan I would like to be able to change out the names, contact info, ect on my own from adobe illustrator.

Industry/Entity Type

Business

Contact Information for Business Card

Double sided with logo on one side and info on the other. Name, Tel, fax, email and west

```html
<!DOCTYPE html>
<html lang="en">
<head>
<meta charset="utf-8">
<title>Kumo Cafe — Business Card</title>
<link rel="stylesheet" href="https://fonts.googleapis.com/css2?family=Montserrat:wght@400;700&family=Quicksand:wght@400;500&display=swap">
<style>
  :root {
    --backdrop: #d9d3cb;
    --card: #ebe6df;
    --card-edge: #d6cfc5;
    --brown: #6b4424;
    --brown-soft: #8a6648;
  }
  * { box-sizing: border-box; margin: 0; padding: 0; }
  html, body {
    width: 1200px; height: 780px; overflow: hidden;
    background: var(--backdrop);
  }
  .canvas {
    position: relative; width: 1200px; height: 780px;
    display: flex; align-items: center; justify-content: center; gap: 70px;
  }
  .card {
    background: radial-gradient(circle at 45% 40%, #f3efe9 0%, var(--card) 70%);
    border-radius: 18px;
    box-shadow: 0 2px 0 var(--card-edge), 0 12px 30px rgba(60, 40, 20, 0.18);
    color: var(--brown);
    position: relative;
  }

  /* Info side */
  .card--info {
    width: 600px; height: 344px;
    display: flex; align-items: center;
    padding: 0 44px;
  }
  .brand {
    display: flex; align-items: center; gap: 14px;
    font-family: "Montserrat", sans-serif; font-weight: 700;
    color: var(--brown); letter-spacing: 0.06em; text-transform: uppercase;
  }
  .brand__mark { background: var(--brown); flex: none; }
  .card--info .brand { flex-direction: column; align-items: center; width: 200px; gap: 16px; font-size: 24px; }
  .card--info .brand__mark { width: 120px; height: 100px; }
  .divider {
    width: 1px; height: 210px; background: var(--brown-soft);
    margin: 0 36px 0 30px; flex: none;
  }
  .details { font-family: "Quicksand", sans-serif; color: var(--brown); }
  .details__name {
    font-family: "Montserrat", sans-serif; font-weight: 700;
    font-size: 25px; letter-spacing: 0.01em; line-height: 1.1;
  }
  .details__role { font-size: 16px; margin-bottom: 22px; }
  .details__address { font-size: 15px; line-height: 1.35; margin-bottom: 10px; }
  .contact { list-style: none; font-size: 15px; line-height: 1.5; }
  .contact li { display: flex; align-items: center; gap: 8px; }
  .contact svg { width: 14px; height: 14px; flex: none; }

  /* Logo side */
  .card--logo {
    width: 300px; height: 500px;
    display: flex; align-items: center; justify-content: center;
  }
  .card--logo .brand { flex-direction: column; gap: 16px; font-size: 26px; }
  .card--logo .brand__mark { width: 130px; height: 110px; }
</style>
</head>
<body>
<main class="canvas">
  <section class="card card--info" aria-label="Business card, contact side">
    <div class="brand">
      <span class="brand__mark"></span>
      <span class="brand__name">Kumo Cafe</span>
    </div>
    <div class="divider"></div>
    <div class="details">
      <p class="details__name">Employee Name</p>
      <p class="details__role">Director</p>
      <p class="details__address">P.O. Box 000, your address<br>Willow Bay, New Zealand</p>
      <ul class="contact">
        <li>
          <svg viewBox="0 0 14 14" aria-hidden="true"><rect width="14" height="14" rx="3" fill="var(--brown)"/><path d="M4.2 3.3l1.4 1.6-.7 1c.6 1.2 1.3 1.9 2.4 2.5l1-.7 1.6 1.4-.8 1.4C6.4 10.2 3.8 7.6 3.4 4.1z" fill="var(--card)"/></svg>
          0123 456 789
        </li>
        <li>
          <svg viewBox="0 0 14 14" aria-hidden="true"><rect width="14" height="14" rx="3" fill="var(--brown)"/><rect x="3" y="4.2" width="8" height="5.6" fill="none" stroke="var(--card)" stroke-width="1"/><path d="M3 4.4l4 3 4-3" fill="none" stroke="var(--card)" stroke-width="1"/></svg>
          hello@kumocafe.jp
        </li>
        <li>
          <svg viewBox="0 0 14 14" aria-hidden="true"><rect width="14" height="14" rx="3" fill="var(--brown)"/><circle cx="7" cy="7" r="3.8" fill="none" stroke="var(--card)" stroke-width="0.9"/><ellipse cx="7" cy="7" rx="1.6" ry="3.8" fill="none" stroke="var(--card)" stroke-width="0.8"/><path d="M3.2 7h7.6" stroke="var(--card)" stroke-width="0.8"/></svg>
          www.kumocafe.jp
        </li>
      </ul>
    </div>
  </section>

  <section class="card card--logo" aria-label="Business card, logo side">
    <div class="brand">
      <span class="brand__mark"></span>
      <span class="brand__name">Kumo Cafe</span>
    </div>
  </section>
</main>
</body>
</html>
```